Veltrano Community Development Planning New web site

Design a new web site. I have a budget of $1,500.00.
Attached on PowerPoint is a complete site plan. Home page and linked pages.
10 - 12 pages. All copy and photos will be supplied. (300dpi)
I have shown them the concept which they like.
No data bases required. Home page with animations dissolving.
They former web site has been taken down. They have been in business 30 years in New Jersey
Colors teal blues and greens
There will be a new logo)being designed)
The text in home page copy will give you a detailed story what they are all about.

files have been approved for Veltrano, Inc.   Tomas is the designer

Industry/Entity Type

Community

```html
<!DOCTYPE html>
<html lang="en">
<head>
<meta charset="utf-8">
<title>Veltrano Community Development Planning</title>
<link href="https://fonts.googleapis.com/css2?family=Open+Sans:wght@400;600;700;800&family=Oswald:wght@500;700&display=swap" rel="stylesheet">
<style>
:root{
  --orange:#ef8a2b;
  --blue:#2a8cc0;
  --ink:#3a3a3a;
  --muted:#777;
  --rule:#e2e2e2;
  --paper:#ffffff;
  --soft:#f4f4f4;
  --nav:#3b3b3b;
  --footer:#2e2e2e;
  --footer-deep:#1f1f1f;
  --bar:#252525;
}
*{box-sizing:border-box;margin:0;padding:0}
html,body{width:1200px;height:2288px;overflow:hidden}
body{font-family:"Open Sans",Arial,sans-serif;color:var(--ink);background:var(--paper);position:relative}
.wrap{position:absolute;left:0;right:0}

/* header + hero */
.hero{top:0;height:600px;background:linear-gradient(180deg,#cfd9de 0%,#e9e4dc 45%,#cbbfb2 100%)}
.hero-art{position:absolute;inset:0}
.brand{position:absolute;left:40px;top:0;width:200px;height:70px;background:var(--paper);display:flex;align-items:center;gap:10px;padding-left:18px;box-shadow:0 2px 6px rgba(0,0,0,.15)}
.brand-mark{width:16px;height:16px;background:var(--orange)}
.brand-name{font-weight:700;font-size:22px;color:var(--ink)}
.main-nav{position:absolute;left:490px;top:22px;width:670px;height:40px;background:rgba(40,40,40,.85);display:flex}
.main-nav a{flex:1;color:#fff;font-size:12px;font-weight:600;text-decoration:none;display:flex;align-items:center;justify-content:center;letter-spacing:.3px}
.main-nav a.active{background:var(--orange)}
.dropdown{position:absolute;left:700px;top:62px;width:140px;background:var(--orange)}
.dropdown a{display:block;color:#fff;font-size:11px;padding:7px 10px;text-decoration:none;border-top:1px solid rgba(255,255,255,.3)}
.slide-caption{position:absolute;left:150px;top:328px;background:rgba(72,150,110,.9);color:#fff;font-weight:700;font-size:30px;padding:8px 22px;letter-spacing:1px}
.slide-arrow{position:absolute;top:280px;width:40px;height:50px;background:rgba(0,0,0,.55);display:flex;align-items:center;justify-content:center}
.slide-arrow.prev{left:0}.slide-arrow.next{right:0}
.dots{position:absolute;left:0;right:0;top:548px;display:flex;justify-content:center;gap:8px}
.dots span{width:9px;height:9px;border-radius:50%;background:rgba(255,255,255,.7)}
.dots span.on{background:var(--nav)}

/* tagline */
.tagline{top:600px;height:100px;padding:28px 60px 0;font-size:16px;line-height:24px;color:var(--ink)}
.tagline b{color:var(--orange);font-weight:700}
.tagline i{color:var(--blue);font-style:normal;font-weight:700}

/* service cards */
.services{top:712px;height:610px;display:flex;gap:28px;padding:0 48px}
.card{flex:1;background:var(--paper);border:1px solid var(--rule);box-shadow:0 2px 6px rgba(0,0,0,.08)}
.card-img{height:268px}
.card h3{font-size:17px;font-weight:700;color:var(--ink);padding:18px 22px 0;line-height:23px;min-height:70px;border-bottom:1px solid var(--rule);margin:0 0 16px}
.card p{font-size:13px;line-height:21px;color:var(--muted);padding:0 22px}

/* results */
.section-label{position:absolute;left:48px;right:48px;display:flex;align-items:center;gap:14px;font-size:14px;font-weight:700;color:var(--orange)}
.section-label::after{content:"";flex:1;height:1px;background:var(--rule)}
.results{top:1340px;height:210px}
.results .section-label{top:0}
.results-img{position:absolute;left:80px;top:56px;width:220px;height:130px}
.results ul{position:absolute;left:340px;top:48px;width:800px;list-style:none}
.results li{font-size:13px;line-height:20px;color:var(--ink);padding-left:16px;position:relative;margin-bottom:6px}
.results li::before{content:"";position:absolute;left:0;top:7px;width:7px;height:7px;background:var(--orange)}

/* projects */
.projects{top:1556px;height:290px}
.projects .section-label{top:0}
.carousel{position:absolute;left:80px;right:80px;top:56px;display:flex;gap:20px}
.project{flex:1}
.project-img{height:165px}
.project h4{font-size:22px;font-weight:800;color:var(--ink);margin-top:12px;letter-spacing:.5px}
.car-arrow{position:absolute;top:112px;width:34px;height:44px;background:#555;display:flex;align-items:center;justify-content:center}
.car-arrow.prev{left:28px}.car-arrow.next{right:28px;background:var(--footer-deep)}

/* footer */
.site-footer{top:1848px;height:392px;background:var(--footer);color:#ddd}
.foot-col{position:absolute;top:40px}
.foot-col h5{font-size:19px;font-weight:400;color:#fff;margin-bottom:18px}
.foot-col h5 b{font-weight:700}
.contact{left:60px;width:230px}
.field{display:flex;align-items:center;gap:8px;margin-bottom:10px}
.field label{width:42px;font-size:11px;color:#bbb}
.field span{flex:1;height:26px;background:#e8e8e8}
.msg{height:90px;background:#e8e8e8;margin:4px 0 10px 50px}
.send{margin-left:auto;display:block;width:110px;height:28px;background:var(--orange);color:#fff;font-size:11px;font-weight:600;text-align:center;line-height:28px}
.member{left:320px;width:200px}
.badge{width:150px;height:62px;background:#4a4a4a;margin-bottom:16px}
.badge.round{width:70px;height:70px;border-radius:50%}
.more{left:610px;width:170px}
.more ul{list-style:none}
.more li{font-size:12px;color:#ccc;line-height:22px}
.foot-brand{position:absolute;left:860px;top:0;width:290px;height:392px;background:var(--footer-deep);padding:40px 26px}
.foot-brand .brand-line{display:flex;align-items:center;gap:10px;border-bottom:1px solid #555;padding-bottom:18px}
.foot-brand .brand-name{color:#fff;font-size:24px}
.slogan{font-family:"Oswald",sans-serif;color:#fff;font-size:30px;line-height:34px;margin-top:22px;font-weight:500}
.get{font-family:"Oswald",sans-serif;color:var(--orange);font-size:48px;line-height:50px;margin-top:26px;font-weight:700}
.social{display:flex;gap:6px;margin-top:20px}
.social span{width:20px;height:20px;border-radius:50%;background:var(--orange)}

.bottom-bar{top:2240px;height:48px;background:var(--bar);color:#aaa;font-size:11px;display:flex;align-items:center;justify-content:space-between;padding:0 48px}
</style>
</head>
<body>

<header class="wrap hero">
  <div class="hero-art" role="img" aria-label="Photograph of a row of colourful model houses on a street"></div>
  <div class="brand"><span class="brand-mark"></span><span class="brand-name">Veltrano</span></div>
  <nav class="main-nav">
    <a href="#">HOME</a>
    <a href="#">OUR COMPANY</a>
    <a href="#" class="active">HOUSING REHAB</a>
    <a href="#">APPLICATIONS</a>
    <a href="#">CONTACT</a>
  </nav>
  <div class="dropdown">
    <a href="#">Housing Rehab</a>
    <a href="#">Affordable Application</a>
  </div>
  <div class="slide-caption">LOREM LIPSUM</div>
  <div class="slide-arrow prev"><svg width="14" height="20" viewBox="0 0 14 20"><path d="M11 2 3 10l8 8" stroke="#fff" stroke-width="3" fill="none"/></svg></div>
  <div class="slide-arrow next"><svg width="14" height="20" viewBox="0 0 14 20"><path d="M3 2l8 8-8 8" stroke="#fff" stroke-width="3" fill="none"/></svg></div>
  <div class="dots"><span></span><span class="on"></span><span></span></div>
</header>

<section class="wrap tagline">
  <b>Community Development</b> Planning * <b>Housing Rehabilitation</b> Administration * National Housing Renewal Office and <i>Urban Development</i> (NHRO) Program Management * Implementation of Programs under the Jurisdiction of State Council of Affordable Homes (SCAH)
</section>

<section class="wrap services">
  <article class="card">
    <div class="card-img" role="img" aria-label="Illustration of a house model resting on architectural plans" style="background:linear-gradient(135deg,#e9eef2,#b9c7d3)"></div>
    <h3>Housing and Relocation</h3>
    <p>In aliquam egestas elit commodo suscipit. Fusce lectus sem, commodo tincidunt ullamcorper quis, viverra et tellus. Quisque ac erat a tellus cursus bibendum eu sit amet nulla. Pellentesque habitant morbi tristique turpis egestas.</p>
  </article>
  <article class="card">
    <div class="card-img" role="img" aria-label="Photograph of a smiling couple at home" style="background:linear-gradient(135deg,#d9d4cc,#8a6a55)"></div>
    <h3>Community and Economic Development</h3>
    <p>In aliquam egestas elit commodo suscipit. Fusce lectus sem, commodo tincidunt ullamcorper quis, viverra et tellus. Quisque ac erat a tellus cursus bibendum eu sit amet nulla. Pellentesque habitant morbi tristique turpis egestas.</p>
  </article>
  <article class="card">
    <div class="card-img" role="img" aria-label="Photograph of a couple reviewing paperwork with an advisor" style="background:linear-gradient(135deg,#e6e9ec,#9aa8b4)"></div>
    <h3>Grants and Funding Opportunities</h3>
    <p>In aliquam egestas elit commodo suscipit. Fusce lectus sem, commodo tincidunt ullamcorper quis, viverra et tellus. Quisque ac erat a tellus cursus bibendum eu sit amet nulla. Pellentesque habitant morbi tristique turpis egestas.</p>
  </article>
</section>

<section class="wrap results">
  <div class="section-label">We get results</div>
  <div class="results-img" role="img" aria-label="Photograph of a house model with keys and documents" style="background:linear-gradient(135deg,#dfe6ea,#9fb3c0)"></div>
  <ul>
    <li>Veltrano designs income based programs to be supported by federal placement before state funding.</li>
    <li>We implement local programs to benefit people seeking access to affordable housing.</li>
    <li>Our experienced staff screen applicants for local affordable housing.</li>
    <li>We give quality persons who have applied for housing rehabilitation assistance proper guidance.</li>
    <li>Through local housing rehabilitation programs, our experienced inspectors determine what improvements are required as eligible units based on local building codes and health and safety issues.</li>
  </ul>
</section>

<section class="wrap projects">
  <div class="section-label">Current Projects</div>
  <div class="car-arrow prev"><svg width="12" height="18" viewBox="0 0 12 18"><path d="M10 2 3 9l7 7" stroke="#fff" stroke-width="3" fill="none"/></svg></div>
  <div class="carousel">
    <div class="project"><div class="project-img" role="img" aria-label="Photograph of a modern apartment building" style="background:linear-gradient(180deg,#9fc1dc,#7d7268)"></div><h4>LAKEWOOD</h4></div>
    <div class="project"><div class="project-img" role="img" aria-label="Photograph of a residential complex with trees" style="background:linear-gradient(180deg,#b9cfe0,#8c8a7a)"></div><h4>LAKEWOOD</h4></div>
    <div class="project"><div class="project-img" role="img" aria-label="Photograph of a brick apartment block" style="background:linear-gradient(180deg,#a8c4da,#8a5a45)"></div><h4>LAKEWOOD</h4></div>
    <div class="project"><div class="project-img" role="img" aria-label="Photograph of a row of colourful townhouses" style="background:linear-gradient(180deg,#a9c6de,#6f6a5e)"></div><h4>LAKEWOOD</h4></div>
  </div>
  <div class="car-arrow next"><svg width="12" height="18" viewBox="0 0 12 18"><path d="M2 2l7 7-7 7" stroke="#fff" stroke-width="3" fill="none"/></svg></div>
</section>

<footer class="wrap site-footer">
  <div class="foot-col contact">
    <h5>Contact <b>Us</b></h5>
    <div class="field"><label>Name</label><span></span></div>
    <div class="field"><label>Email</label><span></span></div>
    <div class="msg"></div>
    <span class="send">Send Message</span>
  </div>
  <div class="foot-col member">
    <h5>Member <b>Of</b></h5>
    <div class="badge"></div>
    <div class="badge round"></div>
    <div class="badge"></div>
  </div>
  <div class="foot-col more">
    <h5>More <b>Information</b></h5>
    <ul>
      <li>About Us</li><li>Housing Rehab</li><li>Affordable Housing</li><li>Applications</li><li>Resources</li><li>News</li><li>Sitemap</li><li>Contacts</li>
    </ul>
  </div>
  <div class="foot-brand">
    <div class="brand-line"><span class="brand-mark"></span><span class="brand-name">Veltrano</span></div>
    <div class="slogan">COMMUNITY<br>DRIVEN<br>PROJECTS</div>
    <div class="get">GET<br>RESULTS</div>
    <div class="social"><span></span><span></span><span></span><span></span><span></span></div>
  </div>
</footer>

<div class="wrap bottom-bar">
  <span>Copyright 2014 - Veltrano, Inc. All right reserved</span>
  <span>"Finding creative solutions to your community problems"</span>
</div>

</body>
</html>
```